Window Washing and Screen Repair Cartoon Mail-Out Postcard

We are a window washing and screen repair company based out of Somerville, Ma called Harbor Crest Window Cleaning and Screen Repair. We clean all types of residential/condominium, commercial windows, as well as mostly any screen repair. We use a top-of-the-line purified water-fed brush and telescoping pole system to reach as far as the 3rd floor windows on most structures. Purified water dries spotless. We also clean interior windows with an organic solution that is non-toxic and not harmful to animals. We'd like to see a design that would communicate our reach (3rd floor windows) and our use of non-toxic cleaning solutions. We envision a small cartoon guy holding a brush pole, cleaning windows of a 3rd story home (maybe the side of the "v" in Harbor Crest could be part of the building?) Maybe a squeegee laying out. Sun is shining off the glass. The water coming off the brush could be dripping into the shrubbery (the water is purified and good for the plants.) Colors would include blue, green, yellow and along those schemes.
Updates

The purpose of the postcard will be to drive people towards our Dealvane we have running currently. We have 3 great deals: $49, $89, $139 packages for window cleaning. This postcard will be mailed and dropped in many customer hot-spots. Added Saturday, April 4, 2015

Target Market(s)

Home and Condo owners

Industry/Entity Type

It Company

Colors
0555a3
0392cd
3176b5
33a6d7
00a990
fbed22
fece3e
ec1f27

Requirements
Must have
• Cartoon ppl, simple cartoons, ambiguous
• Shiny clean window glass
• Sunny day
Nice to have
• great landscape, shrubbery
• should communicate our "Green" practices: purified water, organic window cleaning solution, paper-less

```html
<!DOCTYPE html>
<html lang="en">
<head>
<meta charset="utf-8">
<title>Harbor Crest Window Cleaning Postcard</title>
<link rel="stylesheet" href="https://fonts.googleapis.com/css2?family=Exo+2:ital,wght@0,700;0,800;1,300;1,400;1,800&family=Oswald:wght@600&display=swap">
<style>
  :root {
    --brand-green: #37e87a;
    --price-red: #ff0000;
    --price-green: #37e87a;
    --price-blue: #002f8f;
    --price-yellow: #ffd12a;
    --detail-grey: #c8c8c8;
    --footer-blue: #00288f;
    --accent-blue: #2f5ff0;
    --ink: #111111;
    --white: #ffffff;
    --call-yellow: #ffd12a;
  }
  * { margin: 0; padding: 0; box-sizing: border-box; }
  html, body { width: 1200px; height: 930px; overflow: hidden; background: var(--white); }
  .postcard { position: relative; width: 1200px; height: 930px; background: var(--white); font-family: "Exo 2", sans-serif; }

  .brand-panel {
    position: absolute; left: 0; top: 0; width: 578px; height: 307px;
    background: var(--brand-green);
    box-shadow: 3px 5px 6px rgba(0,0,0,0.35);
    text-align: center;
  }
  .brand-mark {
    position: absolute; left: 0; right: 0; top: 62px;
    display: flex; justify-content: center; align-items: center; gap: 14px;
    font-weight: 800; font-size: 40px; color: var(--ink);
  }
  .brand-mark .dot { width: 26px; height: 26px; border-radius: 50%; background: var(--accent-blue); }
  .brand-name {
    position: absolute; left: 0; right: 0; top: 168px;
    font-style: italic; font-weight: 800; font-size: 70px; color: var(--white);
    letter-spacing: 1px; line-height: 1;
  }
  .brand-tagline {
    position: absolute; left: 0; right: 0; top: 250px;
    font-weight: 700; font-size: 26px; color: var(--ink); line-height: 1;
  }

  .price-row { position: absolute; left: 0; width: 578px; }
  .price-tag {
    position: absolute; left: 0; top: 0; width: 262px; height: 105px;
    font-family: "Oswald", sans-serif; font-weight: 600; font-size: 96px;
    line-height: 105px; text-align: right; padding-right: 14px; color: var(--white);
  }
  .price-detail {
    position: absolute; left: 262px; width: 316px; height: 83px;
    background: var(--detail-grey);
    padding: 10px 0 0 14px;
    font-style: italic; font-weight: 400; font-size: 21px; line-height: 31px; color: var(--ink);
  }
  .row-1 { top: 332px; } .row-1 .price-tag { background: var(--price-red); } .row-1 .price-detail { top: 14px; }
  .row-2 { top: 449px; } .row-2 .price-tag { background: var(--price-green); } .row-2 .price-detail { top: 13px; }
  .row-3 { top: 572px; } .row-3 .price-tag { background: var(--price-blue); } .row-3 .price-detail { top: 7px; }
  .row-4 { top: 692px; } .row-4 .price-tag { background: var(--price-yellow); color: var(--ink); } .row-4 .price-detail { top: 11px; }

  .stamp-box { position: absolute; left: 874px; top: 32px; width: 290px; height: 266px; border: 3px solid var(--ink); }
  .address-lines { position: absolute; left: 660px; top: 476px; }

  .footer {
    position: absolute; left: 0; top: 820px; width: 1200px; height: 110px;
    background: var(--footer-blue); color: var(--white);
    text-align: center; font-style: italic; font-weight: 300; font-size: 22px;
    line-height: 36px; padding-top: 6px;
  }
  .footer .call { color: var(--call-yellow); font-weight: 800; }
</style>
</head>
<body>
<main class="postcard">
  <section class="brand-panel">
    <div class="brand-mark"><span>Harbor Crest</span><span class="dot"></span></div>
    <h1 class="brand-name">HARBOR CREST</h1>
    <p class="brand-tagline">Window Cleaning and Screen Repair</p>
  </section>

  <section class="price-list">
    <div class="price-row row-1">
      <div class="price-tag">$89</div>
      <p class="price-detail">for up to 25 windows<br>(exterior cleaning)</p>
    </div>
    <div class="price-row row-2">
      <div class="price-tag">$139</div>
      <p class="price-detail">for up to 35 windows<br>(exterior cleaning)</p>
    </div>
    <div class="price-row row-3">
      <div class="price-tag">$199</div>
      <p class="price-detail">for up to 25 windows<br>(interior/exterior cleaning)</p>
    </div>
    <div class="price-row row-4">
      <div class="price-tag">$289</div>
      <p class="price-detail">for up to 35 windows<br>(interior/exterior cleaning)</p>
    </div>
  </section>

  <div class="stamp-box"></div>

  <svg class="address-lines" width="492" height="224" viewBox="0 0 492 224">
    <g stroke="#111111" stroke-width="3">
      <line x1="0" y1="2" x2="490" y2="2"/>
      <line x1="0" y1="46" x2="490" y2="46"/>
      <line x1="0" y1="90" x2="490" y2="90"/>
      <line x1="0" y1="134" x2="490" y2="134"/>
      <line x1="0" y1="178" x2="490" y2="178"/>
      <line x1="0" y1="221" x2="490" y2="221"/>
    </g>
  </svg>

  <footer class="footer">
    <p>Free estimates. Service Area includes up to around 30 miles outside of Boston.</p>
    <p>Insured and Bonded. Satisfaction Guaranteed. <span class="call">Call 866 555 0142 FREE</span></p>
  </footer>
</main>
</body>
</html>
```